App Design for Restaurant App

We need a design for the new Mobile App for the Restaurant Volmik. See attachment for presentation sketches.
There are two attached files: File 2 shows the App in general and File 1 shows the five screens which need to be designed. Your work should contain the general color scheme, icons and layout proposal.
Updates
Hi Designers
There where several questions about the scope of the work. We are looking for a design for an App. The promotion website of the restaurant Volmik can be found under www.restaurant-volmik.ch
There you will get an impression of the Corporate Identity used by the restaurant and you will also find the logo.
In the sketch there are several screens which don't need a design, e.g. the cover flow or video screen
please ask if you have any question
kind regards
Tobias
Industry/Entity Type
Restaurant
Look and feel
Each slider illustrates characteristics of the customer's brand and the style your logo design should communicate.

```html
<!DOCTYPE html>
<html lang="de">
<head>
<meta charset="utf-8">
<title>Restaurant Volmik – App Screens</title>
<link href="https://fonts.googleapis.com/css2?family=PT+Sans:wght@400;700&display=swap" rel="stylesheet">
<style>
  :root {
    --olive: #4a5224;
    --olive-dark: #3b4119;
    --cream: #faf6c8;
    --white: #ffffff;
    --ink: #1c1c1c;
    --link: #1f2a8c;
    --photo-a: #c9b28a;
    --photo-b: #f1ece2;
    --photo-c: #8a6a45;
  }
  * { margin: 0; padding: 0; box-sizing: border-box; }
  html, body { width: 1200px; height: 900px; overflow: hidden; background: var(--white); }
  body { position: relative; font-family: "PT Sans", "Myriad Pro", sans-serif; color: var(--olive); }

  .screen { position: absolute; top: 86px; width: 487px; height: 729px; background: var(--cream); border: 1px solid var(--ink); }
  .screen--events { left: 80px; }
  .screen--reservation { left: 636px; }

  .abs { position: absolute; }

  .app-header { left: 47px; top: 19px; width: 391px; height: 122px; background: var(--white); }
  .brand-name { position: absolute; left: 0; right: 0; top: 84px; text-align: center; font-size: 29px; letter-spacing: 0.2px; color: var(--olive); line-height: 1; }
  .menu-icon { position: absolute; right: 6px; top: 37px; width: 48px; height: 48px; }

  .back-tab { left: -3px; top: 45px; width: 101px; height: 43px; }
  .back-tab span { position: absolute; left: 28px; top: 9px; color: var(--white); font-size: 19px; }

  .hero { left: 15px; top: 161px; width: 455px; height: 147px; background: var(--white); padding: 9px 1px 7px; }
  .hero-photo { width: 100%; height: 100%;
    background: linear-gradient(180deg, var(--photo-a) 0%, #e8e2d2 35%, var(--photo-b) 60%, var(--photo-c) 100%); }

  .card { background: var(--white); box-shadow: 5px 5px 0 var(--olive-dark); }
  .section-title { text-align: center; font-size: 28px; color: var(--olive); line-height: 1; }

  .events-title { left: 47px; top: 333px; width: 392px; height: 55px; padding-top: 14px; }
  .events-list { left: 49px; top: 435px; width: 391px; height: 217px; list-style: none; padding-top: 17px; }
  .events-list li { position: relative; height: 51px; padding-left: 53px; font-size: 19px; color: var(--olive); line-height: 28px; }
  .events-list .dot { position: absolute; left: 20px; top: 3px; width: 24px; height: 24px; border-radius: 50%;
    background: radial-gradient(circle at 40% 35%, #8a8f6a 0%, #4d5132 55%, #2f321c 100%); border: 1px solid #222; }
  .events-list .chevron { position: absolute; right: 22px; top: 3px; width: 22px; height: 24px; }

  .reservation-title { left: 46px; top: 326px; width: 392px; height: 42px; padding-top: 5px; }
  .reservation-form { left: 46px; top: 388px; width: 392px; height: 306px; }
  .field-label { position: absolute; left: 26px; font-size: 18px; color: var(--olive-dark); }
  .text-input { position: absolute; left: 118px; width: 257px; height: 34px; border: 3px solid var(--olive); background: var(--white); }
  .time { position: absolute; left: 172px; top: 124px; font-size: 18px; color: var(--link); border-bottom: 3px solid var(--olive); padding: 0 2px 1px; }
  .date { position: absolute; left: 272px; top: 124px; font-size: 18px; color: var(--ink); }
  .spinner { position: absolute; left: 292px; top: 168px; width: 83px; height: 36px; border: 3px solid var(--olive); }
  .spinner span { position: absolute; left: 19px; top: 4px; font-size: 18px; color: var(--ink); }
  .spinner svg { position: absolute; right: 3px; top: 3px; }
  .select { position: absolute; left: 176px; top: 216px; width: 199px; height: 35px; border: 3px solid var(--olive); }
  .select span { position: absolute; left: 42px; top: 4px; font-size: 18px; color: var(--ink); }
  .select svg { position: absolute; right: 0; top: 0; }
  .submit { position: absolute; left: 176px; top: 262px; width: 198px; height: 34px; border: 2px solid var(--olive);
    background: var(--white); box-shadow: 3px 3px 0 var(--olive-dark); text-align: center; font-size: 19px; color: var(--olive-dark); line-height: 30px; }
</style>
</head>
<body>

<!-- Screen: Events -->
<section class="screen screen--events">
  <header class="abs app-header">
    <div class="brand-name">RESTAURANT VOLMIK</div>
    <svg class="menu-icon" viewBox="0 0 48 48" aria-label="Menü">
      <rect x="0" y="0" width="21" height="21" fill="#4a5224"/>
      <rect x="27" y="0" width="21" height="21" fill="#4a5224"/>
      <rect x="0" y="27" width="21" height="21" fill="#4a5224"/>
      <rect x="27" y="27" width="21" height="21" fill="#4a5224"/>
    </svg>
  </header>
  <div class="abs back-tab">
    <svg width="101" height="43" viewBox="0 0 101 43"><path d="M20 0 H101 V43 H20 L0 21.5 Z" fill="#4a5224"/></svg>
    <span>Zurück</span>
  </div>
  <div class="abs hero"><div class="hero-photo" role="img" aria-label="Festlich gedeckter Speisesaal mit weißen Tischen und Stühlen"></div></div>

  <div class="abs card events-title"><h2 class="section-title" style="font-weight:400">EVENTS</h2></div>
  <ul class="abs card events-list">
    <li><span class="dot"></span>Auto-Kino<svg class="chevron" viewBox="0 0 22 24"><path d="M3 2 L19 12 L3 22" fill="none" stroke="#4a5224" stroke-width="5"/></svg></li>
    <li><span class="dot"></span>September - Oktober<svg class="chevron" viewBox="0 0 22 24"><path d="M3 2 L19 12 L3 22" fill="none" stroke="#4a5224" stroke-width="5"/></svg></li>
    <li><span class="dot"></span>Oktober - November<svg class="chevron" viewBox="0 0 22 24"><path d="M3 2 L19 12 L3 22" fill="none" stroke="#4a5224" stroke-width="5"/></svg></li>
    <li><span class="dot"></span>31 Dezember 2012<svg class="chevron" viewBox="0 0 22 24"><path d="M3 2 L19 12 L3 22" fill="none" stroke="#4a5224" stroke-width="5"/></svg></li>
  </ul>
</section>

<!-- Screen: Reservation -->
<section class="screen screen--reservation">
  <header class="abs app-header">
    <div class="brand-name">RESTAURANT VOLMIK</div>
    <svg class="menu-icon" viewBox="0 0 48 48" aria-label="Menü">
      <rect x="0" y="0" width="21" height="21" fill="#4a5224"/>
      <rect x="27" y="0" width="21" height="21" fill="#4a5224"/>
      <rect x="0" y="27" width="21" height="21" fill="#4a5224"/>
      <rect x="27" y="27" width="21" height="21" fill="#4a5224"/>
    </svg>
  </header>
  <div class="abs back-tab">
    <svg width="101" height="43" viewBox="0 0 101 43"><path d="M20 0 H101 V43 H20 L0 21.5 Z" fill="#4a5224"/></svg>
    <span>Zurück</span>
  </div>
  <div class="abs hero"><div class="hero-photo" role="img" aria-label="Festlich gedeckter Speisesaal mit weißen Tischen und Stühlen"></div></div>

  <div class="abs card reservation-title"><h2 class="section-title" style="font-weight:400">RESERVATION</h2></div>
  <div class="abs card reservation-form">
    <span class="field-label" style="top:22px">Name:</span>
    <div class="text-input" style="top:15px"></div>
    <span class="field-label" style="top:72px">Telefon:</span>
    <div class="text-input" style="top:65px"></div>
    <span class="field-label" style="top:124px">Wann:</span>
    <span class="time">19:00</span>
    <span class="date">12.10.2012</span>
    <span class="field-label" style="top:175px">Anzahl Personen</span>
    <div class="spinner"><span>3</span>
      <svg width="18" height="28" viewBox="0 0 18 28"><path d="M9 2 L16 12 H2 Z M9 26 L16 16 H2 Z" fill="#4a5224"/></svg>
    </div>
    <span class="field-label" style="top:226px">Spezialwunsch</span>
    <div class="select"><span>Geburtstag</span>
      <svg width="27" height="29" viewBox="0 0 27 29"><rect x="0" y="0" width="3" height="29" fill="#4a5224"/><path d="M7 9 H21 L14 21 Z" fill="#4a5224"/></svg>
    </div>
    <div class="submit">Bestätigen</div>
  </div>
</section>

</body>
</html>
```